Design einer Preisliste
Zielgruppe
Wir produzieren und verkaufen Suppen Konserven und Konzentrate an Gewerbetreibende + Endabnehmer.
Wir sind im Premium Segment angesiedelt.
Hauptsächlicher Vertrieb erfolgt über den Großhandel
Die Firma ist über 80 Jahre alt
https://www.morvak-eintopf.de/
Aufgabenstellung
Unsere Preisliste soll neu designed werden.
Vorgaben sind:
Hochwertig + Elegant
Eher konservativ gehalten als zu bunt.
Die neuen Preise müssen in die Liste mit eingepflegt werden
Die alte Preisliste und die neuen Preise werden mit beigefügt.

```html
<!DOCTYPE html>
<html lang="de">
<head>
<meta charset="utf-8">
<title>Morvak Großverbraucher Sortimentliste 4/4</title>
<link rel="stylesheet" href="https://fonts.googleapis.com/css2?family=Poppins:ital,wght@0,400;0,500;0,600;0,700;1,400&family=Great+Vibes&display=swap">
<style>
:root{
  --dark:#4a4a49;
  --gold:#b89a57;
  --gold-text:#b5975a;
  --row-a:#efe7dc;
  --row-b:#f7f3ed;
  --terms-bg:#efe7dc;
  --ink:#3a3a3a;
  --veg:#4caf3a;
  --white:#ffffff;
}
*{box-sizing:border-box;margin:0;padding:0}
html,body{width:848px;height:1200px;overflow:hidden;background:var(--white)}
body{position:relative;font-family:"Poppins",sans-serif;color:var(--ink)}
.page-head{position:absolute;top:18px;right:0;height:27px;display:flex;align-items:center}
.brand{font-weight:700;font-size:15px;color:var(--gold-text);margin-right:10px;display:flex;align-items:center;gap:5px}
.brand-dot{width:9px;height:9px;border-radius:50%;background:var(--gold-text)}
.page-head .label{font-size:10px;color:var(--gold-text);margin-right:8px}
.page-head .label b{font-weight:600}
.page-no{background:var(--gold);color:var(--white);width:115px;height:27px;display:flex;align-items:center;justify-content:center;font-size:14px;letter-spacing:1px}
.section{position:absolute;left:0;width:848px}
.bar{height:38px;width:292px;background:var(--dark);color:var(--white);font-weight:600;font-size:17.5px;display:flex;align-items:center;padding-left:61px}
.tagline{position:absolute;left:300px;top:1px;font-family:"Great Vibes",cursive;font-size:27px;color:var(--gold-text);white-space:nowrap}
table{margin:10px 0 0 60px;width:728px;border-collapse:collapse;table-layout:fixed}
th{font-size:8.8px;font-weight:600;line-height:1.2;text-align:center;vertical-align:bottom;padding-bottom:3px;border-bottom:2px solid var(--gold)}
td{font-size:8.8px;text-align:center;height:32px;border-left:2px solid var(--white);vertical-align:middle;line-height:1.45;white-space:nowrap}
td:first-child{border-left:none;text-align:left;padding-left:9px}
tbody tr:nth-child(odd){background:var(--row-a)}
tbody tr:nth-child(even){background:var(--row-b)}
td.ean{text-align:right;padding-right:8px}
td.multi{height:46px;line-height:1.45}
.name{font-weight:600;font-size:11.6px;display:block;line-height:1.2}
.sub{font-size:8.6px;display:block;line-height:1.25}
.veg{color:var(--veg);font-size:8.6px;font-weight:600;margin-left:4px}
.fc{color:var(--gold-text);font-weight:400;font-style:italic}
.terms-band{position:absolute;top:981px;left:0;width:848px;height:37px;background:var(--gold);color:var(--white);font-weight:600;font-size:14.5px;display:flex;align-items:center;justify-content:center}
.terms{position:absolute;top:1018px;left:0;width:848px;height:87px;background:var(--terms-bg);padding:12px 58px 0 61px;font-size:10.2px;line-height:1.4}
.footer{position:absolute;top:1105px;left:0;width:848px;height:95px;background:var(--dark);color:var(--white);font-weight:600;font-size:11.6px;letter-spacing:.3px}
.footer .col{position:absolute;top:13px;line-height:1.27}
.footer .web{position:absolute;left:529px;top:47px}
.footer .brand{position:absolute;right:60px;top:22px;color:var(--white);font-size:19px;margin:0}
.footer .brand-dot{background:var(--white)}
</style>
</head>
<body>
<header class="page-head">
  <div class="brand"><span class="brand-dot"></span>morvak</div>
  <div class="label"><b>GROSSVERBRAUCHER</b> | Sortimentliste</div>
  <div class="page-no">4 / 4</div>
</header>

<section class="section" style="top:60px">
  <h2 class="bar">2-Portionen Suppen</h2>
  <table>
    <colgroup><col style="width:332px"><col style="width:51px"><col style="width:62px"><col style="width:58px"><col style="width:44px"><col style="width:67px"><col style="width:65px"><col style="width:49px"></colgroup>
    <thead><tr><th>Artikel-<br>bezeichnung</th><th>morvak-<br>Nr.</th><th>Dosengröße<br>je Artikel</th><th>Inhalt<br>Dose</th><th>Euro<br>Dose</th><th>Karton<br>Inhalt</th><th>C+C Einheit<br>EAN 40871-</th><th>Preis €<br>Karton</th></tr></thead>
    <tbody>
      <tr><td><span class="name">Kessel-Gulaschsuppe</span><span class="sub">mit rustikaler Einlage</span></td><td>312-1</td><td>1/2 Dose</td><td>425 ml</td><td>1,95</td><td>12 x 1</td><td class="ean">15 3</td><td>23,40</td></tr>
      <tr><td><span class="name">Klare Zwiebelsuppe »Belle Rive« <span class="veg">100 % vegetarisch</span></span><span class="sub">nach französischer Art mit Weißwein</span></td><td>318-1</td><td>1/2 Dose</td><td>425 ml</td><td>1,95</td><td>12 x 1</td><td class="ean">72 8</td><td>23,40</td></tr>
      <tr><td><span class="name">Hühnersuppe</span><span class="sub">Consommé mit Anmut und Charakter, mit Eierstich &amp; Reis</span></td><td>325-1</td><td>1/2 Dose</td><td>425 ml</td><td>1,95</td><td>12 x 1</td><td class="ean">39 1</td><td>23,40</td></tr>
      <tr><td><span class="name">Fruchtige Tomaten-Creme-Suppe <span class="veg">100 % vegetarisch</span></span><span class="sub">Provençale mit Tomatenwürfeln</span></td><td>331-1</td><td>1/2 Dose</td><td>425 ml</td><td>1,95</td><td>12 x 1</td><td class="ean">58 6</td><td>23,40</td></tr>
    </tbody>
  </table>
</section>

<section class="section" style="top:287px">
  <h2 class="bar">Bouillon Ringpull-Dosen</h2>
  <table>
    <colgroup><col style="width:332px"><col style="width:51px"><col style="width:62px"><col style="width:58px"><col style="width:44px"><col style="width:67px"><col style="width:65px"><col style="width:49px"></colgroup>
    <thead><tr><th>Artikel-<br>bezeichnung</th><th>morvak-<br>Nr.</th><th>Dosengröße<br>je Artikel</th><th>Inhalt<br>Dose</th><th>Euro<br>Dose</th><th>Karton<br>Inhalt</th><th>C+C Einheit<br>EAN 40871-</th><th>Preis €<br>Karton</th></tr></thead>
    <tbody>
      <tr><td><span class="name">Rindbouillon</span><span class="sub">kräftig, nach Küchenmeister Art, zum Kochen &amp; Würzen, 20 g/Liter</span></td><td>407-1</td><td>1 kg</td><td>für 50 l</td><td>10,95</td><td>6 x 1</td><td class="ean">00 31470 2</td><td>65,70</td></tr>
      <tr><td><span class="name">Hühnerbouillon doppelt</span><span class="sub">aus besten Zutaten, 40 g/Liter</span></td><td>412-1</td><td>1 kg</td><td>für 25 l</td><td>12,35</td><td>6 x 1</td><td class="ean">00 31560 4</td><td>74,10</td></tr>
    </tbody>
  </table>
</section>

<section class="section" style="top:450px">
  <h2 class="bar">Suppeneinlagen</h2>
  <table>
    <colgroup><col style="width:332px"><col style="width:51px"><col style="width:62px"><col style="width:58px"><col style="width:44px"><col style="width:67px"><col style="width:65px"><col style="width:49px"></colgroup>
    <thead><tr><th>Artikel-<br>bezeichnung</th><th>morvak-<br>Nr.</th><th>Dosengröße<br>je Artikel</th><th>Inhalt<br>Dose</th><th>Euro<br>Dose</th><th>Karton<br>Inhalt</th><th>C+C Einheit<br>EAN 40871-</th><th>Preis €<br>Karton</th></tr></thead>
    <tbody>
      <tr><td><span class="name">Eierstich <span class="fc">Premier</span></span><span class="sub">gewürfelt, nach Küchenmeister Art</span></td><td>503-1</td><td>1/1 Dose</td><td>500 g</td><td>6,45</td><td>12 x 1</td><td class="ean">00 04810 6</td><td>77,40</td></tr>
      <tr><td><span class="name">Markklößchen <span class="fc">Premier</span></span><span class="sub">bestechend im Aussehen - delikat im Geschmack</span></td><td>508-1</td><td>1/1 Dose</td><td style="line-height:1.2">100<br>Klößchen</td><td>7,50</td><td>12 x 1</td><td class="ean">00 04920 3</td><td>90,00</td></tr>
    </tbody>
  </table>
</section>

<section class="section" style="top:612px">
  <h2 class="bar">Eintöpfe</h2>
  <div class="tagline">Spezialitäten aus dem Gemüsegarten</div>
  <table>
    <colgroup><col style="width:332px"><col style="width:51px"><col style="width:62px"><col style="width:58px"><col style="width:44px"><col style="width:67px"><col style="width:65px"><col style="width:49px"></colgroup>
    <thead><tr><th>Artikel-<br>bezeichnung</th><th>morvak-<br>Nr.</th><th>Dosengröße<br>je Artikel</th><th>Inhalt<br>Dose</th><th>Euro<br>Dose</th><th>Karton<br>Inhalt</th><th>C+C Einheit<br>EAN 40871-</th><th>Preis €<br>Karton</th></tr></thead>
    <tbody>
      <tr><td><span class="name">Erbsensuppe - deftig</span></td><td>214-1</td><td>1/1 Dose</td><td>850 ml</td><td>2,65</td><td>12 x 1</td><td class="ean">27 5</td><td>31,80</td></tr>
      <tr><td><span class="name">Kartoffelsuppe - rustikale</span></td><td>216-1</td><td>1/1 Dose</td><td>850 ml</td><td>2,65</td><td>12 x 1</td><td class="ean">27 5</td><td>31,80</td></tr>
      <tr><td><span class="name">Linsen-Suppe - Terrine</span></td><td>219-1</td><td>1/1 Dose</td><td>850 ml</td><td>2,65</td><td>12 x 1</td><td class="ean">00 05740 8</td><td>31,80</td></tr>
    </tbody>
  </table>
</section>

<section class="section" style="top:807px">
  <h2 class="bar">Fleischkonserven</h2>
  <div class="tagline">in hervorragender Qualität</div>
  <table>
    <colgroup><col style="width:332px"><col style="width:51px"><col style="width:62px"><col style="width:58px"><col style="width:44px"><col style="width:67px"><col style="width:65px"><col style="width:49px"></colgroup>
    <thead><tr><th>Artikel-<br>bezeichnung</th><th>morvak-<br>Nr.</th><th>Dosengröße<br>je Artikel</th><th>Inhalt<br>Dose</th><th>Euro<br>Dose</th><th>Karton<br>Inhalt</th><th>C+C Einheit<br>EAN 40871-</th><th>Preis €<br>Karton</th></tr></thead>
    <tbody>
      <tr><td><span class="name">Echt Hanseatischer Labskaus</span><span class="sub">vom Kapitänstisch</span></td><td>604-1</td><td>1/1 Dose</td><td>850 ml</td><td>4,45</td><td>12 x 1</td><td class="ean">00 06150 9</td><td>53,40</td></tr>
      <tr><td class="multi"><span class="name">Ragoût fin »Gascogner Art« <span class="fc">Exquisit</span></span><span class="sub">aus Kalb &amp; Geflügel, ohne Brät und ohne Farce</span></td><td class="multi">611-1<br>&nbsp;<br>615-1</td><td class="multi">1/4 Ring-Pull<br>&nbsp;<br>1/1 Dose</td><td class="multi" style="font-size:8.3px">1 große Port.<br>&nbsp;<br>4 große Port.</td><td class="multi">3,25<br>&nbsp;<br>10,00</td><td class="multi">50 = 10 x 5<br>24 x 1/4<br>12 x 1</td><td class="multi ean">00 06230 7<br>38 2<br>00 06270 1</td><td class="multi">162,50<br>78,00<br>120,00</td></tr>
    </tbody>
  </table>
</section>

<div class="terms-band">Lieferungs- &amp; Zahlungsbedingungen</div>
<div class="terms">Die Preise verstehen sich frei Haus und ohne MwSt.. Die Ware bleibt bis zur vollständigen Bezahlung unser Eigentum. Sie kann nur im ordnungsgemäßigen Geschäftsverkehr weiterveräußert werden. Der Käufer tritt jedoch die Forderung, die sich aus der Weiterveräußerung der Vorbehaltsware ergeben, in jedem Falle an uns ab. Eine Sicherungsübereignung der Vorbehaltsware ist ausgeschlossen.<br>Zahlung 30 Tage nach Rechnungsdatum netto Kasse. Erfüllungsort und Gerichtsstand der Lieferung und Zahlung ist der Sitz der Firma:<br>Morvak &amp; Co. GmbH &amp; Co. KG, D-41234 Wendorf.</div>

<footer class="footer">
  <div class="col" style="left:61px">Morvak &amp; Co. GmbH &amp; Co. KG<br>Lindenallee 12–18<br>D-41234 Wendorf</div>
  <div class="col" style="left:280px">Telefon: +49-(0)-2190-44120<br>Telefax : +49-(0)-2190-44129<br>E-Mail &nbsp;: info@morvak-eintopf.de</div>
  <div class="web">www.morvak-eintopf.de</div>
  <div class="brand"><span class="brand-dot"></span>morvak</div>
</footer>
</body>
</html>
```